Business Cards for an 'affordable luxury' inner city home builder in Calgary.

We need a business card design that emulates the progressive, innovative, culture of our company and the modern style of our homes. Use our website www.velmarcrest-ab.com as a reference for the product we build.

Our company builds homes in the inner city space of Calgary, Alberta. We build affordable luxury.

Target Market(s)

Young professional Families

Contact Information for Business Card

Try to maintain consistency with the logo font and the card font.

Requirements
Must have
• The details must include: Name, education, title, phone number, website and email (Address is not as important)
• The design must be uniques (like our logo), elegant, sophisticated and modern.

```html
<!DOCTYPE html>
<html lang="en">
<head>
<meta charset="utf-8">
<title>Velmarcrest Homes Ltd — Business Cards</title>
<link href="https://fonts.googleapis.com/css2?family=Raleway:wght@400;500;700&display=swap" rel="stylesheet">
<style>
  :root {
    --backdrop: #e8e8ea;
    --card-white: #ffffff;
    --card-black: #1f1f1f;
    --ink: #1a1a1a;
    --ink-soft: #3a3a3a;
    --muted: #8a8a8a;
    --rule: #b5b5b5;
    --paper-white: #f4f4f4;
  }
  * { box-sizing: border-box; margin: 0; padding: 0; }
  html, body {
    width: 1200px; height: 800px; overflow: hidden;
    background: var(--backdrop);
    font-family: "Raleway", sans-serif;
  }
  .stage {
    width: 1200px; height: 800px;
    display: flex; align-items: center; justify-content: center; gap: 60px;
  }
  .card {
    width: 520px; height: 297px; position: relative;
    box-shadow: 0 6px 18px rgba(0,0,0,0.12);
  }
  .card--front { background: var(--card-white); padding: 34px 40px 0 40px; }
  .card--back { background: var(--card-black); overflow: hidden; }

  .brand { display: flex; align-items: center; gap: 14px; }
  .brand__square { width: 34px; height: 34px; border: 2px solid currentColor; flex: none; }
  .brand__name {
    font-weight: 700; font-size: 19px; line-height: 1.05;
    letter-spacing: 0.5px; text-transform: uppercase;
  }
  .card--front .brand { color: var(--ink); }

  .person { margin-top: 26px; margin-left: 48px; }
  .person__name { font-weight: 700; font-size: 15px; color: var(--ink); }
  .person__creds { color: var(--muted); font-weight: 700; }
  .person__role { font-size: 13px; color: var(--ink-soft); line-height: 1.35; }

  .divider { height: 1px; background: var(--rule); margin: 10px 0 10px 48px; width: 250px; }

  .contact { list-style: none; margin-left: 48px; }
  .contact li {
    display: flex; align-items: center; gap: 7px;
    font-size: 13px; color: var(--ink-soft); line-height: 1.45;
  }
  .contact svg { width: 11px; height: 11px; flex: none; }

  .baseline {
    position: absolute; left: 40px; right: 40px; bottom: 26px;
    height: 1px; background: var(--rule);
  }

  .back__pattern {
    position: absolute; inset: 0;
    background: linear-gradient(135deg, #242424, #1b1b1b);
  }
  .card--back .brand {
    position: absolute; left: 50%; top: 50%;
    transform: translate(-50%, -50%);
    color: var(--paper-white);
  }
  .card--back .brand__name { font-size: 22px; }
</style>
</head>
<body>
<main class="stage">
  <section class="card card--front" aria-label="Business card front">
    <div class="brand">
      <span class="brand__square"></span>
      <span class="brand__name">Velmarcrest<br>Homes Ltd</span>
    </div>
    <div class="person">
      <p class="person__name">Jasveer<span class="person__creds">, P.ENG, MBA</span></p>
      <p class="person__role">Co-Founder<br>Business Development / Strategy</p>
    </div>
    <div class="divider"></div>
    <ul class="contact">
      <li>
        <svg viewBox="0 0 12 12" aria-hidden="true"><path d="M2.5 1h2l1 2.5-1.3 1a6 6 0 0 0 3.3 3.3l1-1.3L11 7.5v2a1 1 0 0 1-1 1A9 9 0 0 1 1.5 2a1 1 0 0 1 1-1z" fill="#555"/></svg>
        403-555-0148
      </li>
      <li>
        <svg viewBox="0 0 12 12" aria-hidden="true"><rect x="0.75" y="2.25" width="10.5" height="7.5" fill="none" stroke="#555" stroke-width="1.2"/><path d="M1 2.5 6 6.5 11 2.5" fill="none" stroke="#555" stroke-width="1.2"/></svg>
        jasveer@velmarcrest-ab.com
      </li>
      <li>
        <svg viewBox="0 0 12 12" aria-hidden="true"><circle cx="6" cy="6" r="5" fill="none" stroke="#555" stroke-width="1.1"/><ellipse cx="6" cy="6" rx="2.2" ry="5" fill="none" stroke="#555" stroke-width="1"/><path d="M1 6h10" stroke="#555" stroke-width="1"/></svg>
        www.velmarcrest-ab.com
      </li>
    </ul>
    <div class="baseline"></div>
  </section>

  <section class="card card--back" aria-label="Business card back">
    <div class="back__pattern" role="img" aria-label="Subtle dark tone-on-tone repeating pattern"></div>
    <div class="brand">
      <span class="brand__square"></span>
      <span class="brand__name">Velmarcrest<br>Homes Ltd</span>
    </div>
  </section>
</main>
</body>
</html>
```